Patient Report Folder for modern Chiropractic Clinic

We are looking for someone to design a patient folder and 3 simple info sheets to go along with it.

The design should be clean and masculine with an artsy touch. I am a fan of the Del Morano style drawings so would like the background to be a style of parchment paper. The info sheets should follow a similar style.

Please check the “Design Outline” pdf and the “Folder Design” file before getting started. The 3 info sheets are going to be placed in the pocket where “Attachment #3” will be.

- The format should be DIN A4 according to the printing details attached in the files section. Please see the ''Folder Design.jpg'' for the design of the folder.
- All the designs should be different and unique in nature but match each other.
- The text for Info Sheet #3 can be left blank.

It is probably best to take a look at the ''Design Outline'' file first to see how I envision the design to be. Please do not hesitate to ask me questions or to discuss ideas.

Target Market(s)

upper class audience with a focus on health and well-being

Industry/Entity Type

Chiropractic // Health

Requirements
Must have
• The colours should be fitting with the main colours in the logo: #1ccad5 and #b1b2b4
Nice to have
• Del Morano Style design and the background on parchment paper style. It is not a must but if anyone can come up with a suitable design and colorway that would be great.

```html
<!DOCTYPE html>
<html lang="en">
<head>
<meta charset="utf-8">
<title>Spinewell Patient Folder – Dieline</title>
<link rel="stylesheet" href="https://fonts.googleapis.com/css2?family=Arimo:wght@400&display=swap">
<style>
  :root {
    --stage: #b2c5c2;
    --flap: #a0b6b3;
    --mint: #57f7b8;
    --mint-deep: #4eeab0;
    --parchment-light: #f8f7f5;
    --parchment-edge: #e9d6bb;
    --pocket-dark: #5c5c5c;
    --cut-line: #6cf06c;
    --fold-line: #e0323a;
    --bleed-line: #5fd3e6;
    --ink: #2c2c2c;
    --white: #ffffff;
  }
  html, body {
    margin: 0;
    padding: 0;
    overflow: hidden;
    background: var(--stage);
  }
  .canvas {
    display: block;
    width: 810px;
    height: 1200px;
    background: var(--stage);
    font-family: "Arimo", Arial, sans-serif;
  }
  .contact-line { font-size: 7px; fill: var(--white); }
  .site-line { font-size: 7px; fill: var(--ink); }
  .brand-name { font-size: 24px; fill: var(--mint-deep); letter-spacing: 1px; }
  .brand-faint { font-size: 34px; fill: var(--white); opacity: 0.08; letter-spacing: 2px; }
  .fold { stroke: var(--fold-line); stroke-width: 0.7; stroke-dasharray: 3 2; fill: none; }
  .bleed { stroke: var(--bleed-line); stroke-width: 0.6; stroke-dasharray: 3 2; fill: none; }
  .cut { stroke: var(--cut-line); stroke-width: 0.7; fill: none; }
</style>
</head>
<body>
<svg class="canvas" viewBox="0 0 810 1200" xmlns="http://www.w3.org/2000/svg">
  <defs>
    <radialGradient id="parchment" cx="50%" cy="50%" r="70%">
      <stop offset="0%" stop-color="#f8f7f5"/>
      <stop offset="55%" stop-color="#f6f3ee"/>
      <stop offset="100%" stop-color="#e6cfb0"/>
    </radialGradient>
    <radialGradient id="mint-wash" cx="50%" cy="55%" r="75%">
      <stop offset="0%" stop-color="#5af8bb"/>
      <stop offset="70%" stop-color="#57f7b8"/>
      <stop offset="100%" stop-color="#4fe3a8"/>
    </radialGradient>
  </defs>

  <!-- Outside of folder -->
  <g class="folder-outside">
    <polygon class="side-flap" points="138,278 166,271 166,435 152,431 138,424" fill="var(--flap)"/>
    <path class="bottom-pocket-back" d="M168,438 H416 V489 Q414,507 396,515 L168,602 Z" fill="var(--flap)"/>
    <path class="cut" d="M416,438 V489 Q414,507 396,515 L168,602"/>

    <rect class="back-cover" x="166" y="81" width="253" height="357" fill="url(#mint-wash)" role="img" aria-label="Mint green textured watercolour wash"/>
    <circle class="back-cover-ring" cx="292" cy="249" r="108" fill="none" stroke="var(--white)" stroke-opacity="0.1" stroke-width="2"/>
    <text class="brand-faint" x="292" y="261" text-anchor="middle">SPINEWELL</text>

    <text class="contact-line" x="294" y="402" text-anchor="middle">12 Maple Row, Halden, Canada 20418</text>
    <text class="contact-line" x="294" y="411" text-anchor="middle">&#9742; 555-210-4187 · 555-398-6620 · hello@spinewell.com</text>
    <text class="contact-line" x="292" y="420" text-anchor="middle">www.spinewell.com</text>

    <rect class="front-cover" x="419" y="81" width="255" height="353" fill="url(#parchment)" role="img" aria-label="Aged parchment paper texture"/>
    <circle class="brand-ring" cx="540" cy="226" r="39" fill="none" stroke="var(--mint)" stroke-width="1.6"/>
    <text class="brand-name" x="545" y="293" text-anchor="middle">SPINEWELL</text>
    <text class="site-line" x="545" y="414" text-anchor="middle">www.spinewell.com</text>
  </g>

  <!-- Inside of folder -->
  <g class="folder-inside">
    <rect class="inner-spread" x="177" y="657" width="472" height="330" fill="url(#parchment)" role="img" aria-label="Aged parchment paper texture"/>
    <rect class="cut" x="177" y="657" width="472" height="330"/>
    <rect class="bleed" x="183" y="662" width="460" height="320"/>
    <line class="fold" x1="410" y1="657" x2="410" y2="987"/>
    <line class="fold" x1="416" y1="657" x2="416" y2="987"/>

    <path class="inner-pocket" d="M420,929 Q420,912 448,905 L648,835 H653 L675,841 V977 L653,987 H648 V1144 L432,1064 Q420,1057 420,1037 Z" fill="var(--pocket-dark)"/>
    <path class="cut" d="M648,987 V1144 L432,1064 Q420,1057 420,1037 V981 M653,835 L675,841 V977 L653,987"/>
    <path class="bleed" d="M424,981 H425 V1030 Q426,1050 438,1057 L643,1134 V840"/>
    <line class="fold" x1="420" y1="987" x2="653" y2="987"/>
    <line class="fold" x1="420" y1="992" x2="653" y2="992"/>
    <line class="fold" x1="650" y1="835" x2="650" y2="987"/>
    <line class="fold" x1="654" y1="838" x2="654" y2="987"/>
    <line class="cut" x1="518" y1="1014" x2="616" y2="1014"/>
  </g>
</svg>
</body>
</html>
```